Income Tax Business Cards - Updates

Need to update these business cards while keeping all the same wording but just update them and make them look nicer and more modern/ on brand with our brand.

Industry/Entity Type

finance

Contact Information for Business Card

we have multiple locations so will just need to easily be able to change the address and phone numbers

Colors

Designer to choose colors to be used in the design.

```html
<!DOCTYPE html>
<html lang="en">
<head>
<meta charset="utf-8">
<title>Tax Season Business Card – Front and Back</title>
<link rel="stylesheet" href="https://fonts.googleapis.com/css2?family=Montserrat:wght@500;600;700;800;900&display=swap">
<style>
  :root {
    --brand-green: #155130;
    --brand-red: #c1272d;
    --paper: #ffffff;
    --ink: #1c1c1c;
    --backdrop: #ecebe7;
  }
  * { box-sizing: border-box; margin: 0; padding: 0; }
  html, body {
    width: 1200px;
    height: 800px;
    overflow: hidden;
    background: var(--backdrop);
    font-family: "Montserrat", Arial, sans-serif;
  }
  .sheet {
    width: 1200px;
    height: 800px;
    display: flex;
    flex-direction: column;
    align-items: center;
    justify-content: center;
    gap: 50px;
  }
  .card {
    position: relative;
    width: 540px;
    height: 309px;
    overflow: hidden;
    box-shadow: 0 6px 18px rgba(0,0,0,0.18);
  }

  /* Front */
  .card-front { background: var(--paper); display: flex; flex-direction: column; }
  .offer-panel {
    height: 150px;
    background: var(--brand-green);
    color: var(--paper);
    display: flex;
    flex-direction: column;
    align-items: center;
    justify-content: center;
    text-align: center;
    padding-top: 6px;
  }
  .offer-amount { font-weight: 900; font-size: 50px; line-height: 1; letter-spacing: 0.5px; }
  .offer-label { font-weight: 800; font-size: 29px; line-height: 1.1; margin-top: 4px; }
  .offer-note { font-weight: 700; font-size: 13px; margin-top: 5px; letter-spacing: 0.3px; }
  .estimate-band {
    height: 40px;
    background: var(--brand-red);
    color: var(--paper);
    font-weight: 800;
    font-size: 25px;
    display: flex;
    align-items: center;
    justify-content: center;
    letter-spacing: 0.5px;
  }
  .contact-panel {
    flex: 1;
    display: flex;
    align-items: center;
    justify-content: space-between;
    padding: 0 34px 0 40px;
  }
  .brand-name {
    display: flex;
    align-items: center;
    gap: 10px;
    color: var(--brand-green);
    font-weight: 700;
    font-size: 21px;
    line-height: 1.15;
  }
  .brand-square { width: 16px; height: 16px; background: var(--brand-green); flex: none; }
  .contact-details { color: var(--ink); text-align: left; }
  .contact-phone { font-weight: 600; font-size: 22px; margin-bottom: 4px; }
  .contact-line { font-weight: 500; font-size: 13px; line-height: 1.45; }

  /* Back */
  .card-back {
    background: var(--brand-green);
    color: var(--paper);
    display: flex;
    flex-direction: column;
    align-items: center;
    justify-content: center;
    text-align: center;
  }
  .corner-arrow { position: absolute; width: 84px; height: 84px; }
  .corner-arrow-top { top: 0; right: 0; }
  .corner-arrow-bottom { bottom: 0; left: 0; }
  .back-headline { font-weight: 900; font-size: 44px; line-height: 1.02; }
  .back-divider { width: 300px; height: 4px; background: var(--paper); border-radius: 2px; margin: 16px 0 14px; }
  .back-amount { font-weight: 900; font-size: 44px; line-height: 1; }
  .back-label { font-weight: 800; font-size: 27px; margin-top: 4px; }
</style>
</head>
<body>
<main class="sheet">

  <section class="card card-front" aria-label="Business card front">
    <div class="offer-panel">
      <p class="offer-amount">UP TO $6,000</p>
      <p class="offer-label">SAME DAY ADVANCE</p>
      <p class="offer-note">ON APPROVED TAX RETURNS!</p>
    </div>
    <div class="estimate-band">FREE ESTIMATES!</div>
    <div class="contact-panel">
      <div class="brand-name">
        <span class="brand-square"></span>
        <span>Ledger 7<br>Financial Group</span>
      </div>
      <div class="contact-details">
        <p class="contact-phone">(555)555-5555</p>
        <p class="contact-line">Address Line 1</p>
        <p class="contact-line">Address Line 2</p>
        <p class="contact-line">Address Line 3</p>
      </div>
    </div>
  </section>

  <section class="card card-back" aria-label="Business card back">
    <svg class="corner-arrow corner-arrow-top" viewBox="0 0 84 84" aria-hidden="true">
      <polygon points="84,6 84,76 14,76" fill="var(--paper)"/>
      <polygon points="80,16 80,70 26,70" fill="var(--brand-red)"/>
    </svg>
    <svg class="corner-arrow corner-arrow-bottom" viewBox="0 0 84 84" aria-hidden="true">
      <polygon points="0,8 70,8 0,78" fill="var(--paper)"/>
      <polygon points="4,14 58,14 4,68" fill="var(--brand-red)"/>
    </svg>
    <p class="back-headline">FILE YOUR<br>TAXES HERE</p>
    <div class="back-divider"></div>
    <p class="back-amount">UP TO $6,000</p>
    <p class="back-label">SAME DAY ADVANCE</p>
  </section>

</main>
</body>
</html>
```